Vemtra Group: Business Card for a high end technology company

We need a cool new design for our business cards using our cloud logo. We are a technology consulting business. We pride ourselves on be the best of the best. We mainly focus on cloud solutions and managed services. We need a business card that sets us apart from the other technology companies in the area and allows us to stand out.

Target Market(s)

Technology departments, CIO, CEOs, and Information Technology Staff.

Industry/Entity Type

Information Technology

Contact Information for Business Card

Must have the logo and our name.
Must have employee name, email address, office phone, cell phone and website.
Need to have all info on one side a cool design on backside.

Font styles to use
Serif
Sans Serif

Requirements
Must have
• Must have the logo and our name.
• Must have employee name, email address, office phone, cell phone and website.
• Need to have all info on one side a cool design on back side.
• Must be a crisp clean design, not too busy or confusing.

```html
<!DOCTYPE html>
<html lang="en">
<head>
<meta charset="utf-8">
<title>Vemtra Group – Business Card</title>
<link href="https://fonts.googleapis.com/css2?family=Open+Sans:wght@400;600;700&display=swap" rel="stylesheet">
<style>
  :root {
    --stage: #2b2b2d;
    --brand-blue: #1b6fbf;
    --brand-blue-light: #3a8fdc;
    --accent-blue: #2f7fd6;
    --panel-dark: #333335;
    --paper: #ffffff;
    --ink: #2a2a2c;
    --ink-light: #f2f2f2;
  }
  * { box-sizing: border-box; margin: 0; padding: 0; }
  html, body { width: 1200px; height: 900px; overflow: hidden; }
  body {
    background: var(--stage);
    font-family: "Open Sans", Arial, sans-serif;
    display: flex;
    flex-direction: column;
    align-items: center;
    justify-content: center;
    gap: 40px;
  }
  .card {
    position: relative;
    width: 700px;
    height: 400px;
    border-radius: 22px;
    overflow: hidden;
    box-shadow: 0 10px 30px rgba(0,0,0,.45);
  }
  /* Front */
  .card-front {
    background: linear-gradient(135deg, var(--brand-blue) 0%, var(--brand-blue-light) 100%);
    display: flex;
    flex-direction: column;
    align-items: center;
    justify-content: center;
    color: var(--paper);
  }
  .brand-name {
    display: flex;
    align-items: center;
    gap: 16px;
    font-weight: 600;
    font-size: 54px;
    letter-spacing: .5px;
    white-space: nowrap;
  }
  .brand-dot {
    width: 26px; height: 26px;
    border-radius: 50%;
    background: currentColor;
    flex: none;
  }
  .front-web {
    margin-top: 14px;
    font-weight: 700;
    font-size: 18px;
    letter-spacing: .5px;
  }
  /* Back */
  .card-back { background: var(--paper); }
  .back-shape { position: absolute; inset: 0; }
  .back-brand {
    position: absolute;
    left: 44px;
    top: 200px;
    color: var(--ink);
    font-size: 36px;
    gap: 12px;
  }
  .back-brand .brand-dot { width: 18px; height: 18px; background: var(--accent-blue); }
  .contact-block {
    position: absolute;
    right: 44px;
    top: 70px;
    text-align: right;
    color: var(--ink-light);
    white-space: nowrap;
  }
  .person-name {
    font-weight: 700;
    font-size: 24px;
    letter-spacing: 1px;
    text-transform: uppercase;
  }
  .person-role {
    color: var(--accent-blue);
    font-size: 15px;
    margin-bottom: 30px;
  }
  .contact-list { list-style: none; }
  .contact-item {
    display: flex;
    justify-content: flex-end;
    align-items: center;
    gap: 10px;
    font-size: 15px;
    line-height: 26px;
  }
  .contact-icon { width: 14px; height: 14px; fill: none; stroke: var(--accent-blue); stroke-width: 1.6; flex: none; }
</style>
</head>
<body>

<section class="card card-front">
  <div class="brand-name"><span class="brand-dot"></span>Vemtra Group</div>
  <div class="front-web">www.vemtragroup.com</div>
</section>

<section class="card card-back">
  <svg class="back-shape" viewBox="0 0 700 400" aria-hidden="true">
    <path d="M290 0 Q 430 140 380 400 L700 400 L700 0 Z" fill="var(--panel-dark)"/>
    <path d="M279 0 Q 421 140 370 400" fill="none" stroke="var(--accent-blue)" stroke-width="6"/>
  </svg>

  <div class="brand-name back-brand"><span class="brand-dot"></span>Vemtra Group</div>

  <div class="contact-block">
    <div class="person-name">Daniel Morrow</div>
    <div class="person-role">Director</div>
    <ul class="contact-list">
      <li class="contact-item">555.210.8499
        <svg class="contact-icon" viewBox="0 0 14 14"><path d="M3 1 L5 1 L6 4 L4.5 5 Q6 8.5 9 9.5 L10 8 L13 9 L13 11 Q12 13 10 13 Q2 11 1 3 Q1 1 3 1 Z"/></svg>
      </li>
      <li class="contact-item">555.210.7488
        <svg class="contact-icon" viewBox="0 0 14 14"><rect x="3.5" y="1" width="7" height="12" rx="1.5"/><line x1="6" y1="11" x2="8" y2="11"/></svg>
      </li>
      <li class="contact-item">info@vemtragroup.com
        <svg class="contact-icon" viewBox="0 0 14 14"><rect x="1" y="3" width="12" height="8" rx="1"/><path d="M1 3 L7 8 L13 3"/></svg>
      </li>
      <li class="contact-item">www.vemtragroup.com
        <svg class="contact-icon" viewBox="0 0 14 14"><circle cx="7" cy="7" r="6"/><ellipse cx="7" cy="7" rx="2.5" ry="6"/><line x1="1" y1="7" x2="13" y2="7"/></svg>
      </li>
    </ul>
  </div>
</section>

</body>
</html>
```